Hold Each Morning As A MOSSbright Harbour

Hello Designers! We need a captivating notebook cover design for our self-development company for people with disabilities. We help people with a diagnosis see everyday as a MOSSBRIGHT HARBOUR than something to ensure. This notebook is to capture the brightness and positivity of everyday, that your struggles are meant for you to overcome. We would like to see designs that follow with our brand (uploaded) and I've also added our logo and kind of notebook as a guide. The final design should be inviting and bright. Use the title "Keep Each Morning A Quiet Lantern". Will decide the words once the background design is finalized

Notebook Size: 8.5 x 5.75 inches
Updates

Hello Designers! I'm extending the deadline to give you an opportunity to submit different and unique designs for the MOSSbright HARBOUR Journal. I've given feedback to most of you so this is your opportunity to try something new. Looking for clean, inviting and unique designs that use the logo colour scheme (attached -- navy blue, light blue, yellow, black). Preferably front and back cover designs.

Target Market(s)

Between 25-35 years

Font styles to use
Serif
Sans Serif
Decorative
Script

Colors
0255a3
fbed22

Requirements
Must have
• -Use colour scheme as per attachment as main colours (can go beyond for contrast ex. pinks/purples/indigo/etc)
Nice to have
• Would like to see designs related to nature, art and/or graphic prints.
Should not have
• icons (no stick figures), silhouettes of people, no hands
• NO stock images

```html
<!DOCTYPE html>
<html lang="en">
<head>
<meta charset="utf-8">
<title>Perrin's Mossbright Harbour – Journal Cover</title>
<link href="https://fonts.googleapis.com/css2?family=Arimo:wght@400&family=Sacramento&display=swap" rel="stylesheet">
<style>
  :root {
    --navy: #0255a3;
    --navy-deep: #024a90;
    --mid-blue: #1f78c8;
    --sky: #3fa4e0;
    --sky-pale: #8fd0f2;
    --leaf-white: #f2f8fc;
    --sun: #fbed22;
  }
  html, body {
    margin: 0;
    padding: 0;
    overflow: hidden;
    background: var(--navy);
  }
  .cover {
    position: relative;
    width: 876px;
    height: 1200px;
    overflow: hidden;
    background: var(--navy);
  }
  .foliage {
    position: absolute;
    left: 0;
    width: 876px;
  }
  .foliage-top { top: 0; height: 460px; }
  .foliage-bottom { bottom: 0; height: 330px; }
  .title-name {
    position: absolute;
    left: 0;
    top: 360px;
    width: 900px;
    margin: 0;
    text-align: center;
    font-family: "Sacramento", "Brush Script MT", cursive;
    font-weight: 400;
    font-size: 250px;
    line-height: 1;
    letter-spacing: 10px;
    color: var(--sun);
  }
  .title-tagline {
    position: absolute;
    left: 217px;
    top: 644px;
    margin: 0;
    font-family: "Arimo", Arial, sans-serif;
    font-weight: 400;
    font-size: 29px;
    line-height: 1;
    letter-spacing: -0.3px;
    color: #ffffff;
  }
</style>
</head>
<body>
  <main class="cover">
    <svg class="foliage foliage-top" viewBox="0 0 876 460" role="img" aria-label="Tropical palm and monstera leaves in yellow, light blue and white framing the top left corner and top edge">
      <defs>
        <linearGradient id="top-sky" x1="0" y1="0" x2="0" y2="1">
          <stop offset="0" stop-color="#8fd0f2"/>
          <stop offset="1" stop-color="#3fa4e0"/>
        </linearGradient>
        <linearGradient id="top-mid" x1="0" y1="0" x2="1" y2="1">
          <stop offset="0" stop-color="#3fa4e0"/>
          <stop offset="1" stop-color="#1f78c8"/>
        </linearGradient>
        <linearGradient id="top-far" x1="0" y1="0" x2="1" y2="0">
          <stop offset="0" stop-color="#1f78c8"/>
          <stop offset="1" stop-color="#0a62b0"/>
        </linearGradient>
      </defs>
      <path d="M480 0 H876 V190 C800 160 720 150 640 120 C580 95 520 60 480 0 Z" fill="url(#top-far)" opacity="0.7"/>
      <path d="M120 0 H600 C590 60 540 110 470 160 C420 200 360 230 280 250 C230 200 180 140 120 0 Z" fill="url(#top-sky)" opacity="0.85"/>
      <path d="M0 90 C80 110 170 150 230 210 C290 270 300 350 260 410 C210 440 150 430 90 400 C50 380 20 360 0 340 Z" fill="url(#top-mid)"/>
      <path d="M300 0 H470 C460 40 420 70 370 80 C330 60 310 30 300 0 Z" fill="#eaf5fc" opacity="0.7"/>
      <path d="M0 0 H230 C210 60 160 120 100 170 C60 200 30 220 0 235 Z" fill="#fbed22"/>
    </svg>

    <h1 class="title-name">Perrin's</h1>
    <p class="title-tagline">MOSSBRIGHT HARBOUR</p>

    <svg class="foliage foliage-bottom" viewBox="0 0 876 330" role="img" aria-label="Band of tropical ferns and palm leaves in white and light blue with a yellow flower along the bottom edge">
      <defs>
        <linearGradient id="bottom-fade" x1="0" y1="0" x2="0" y2="1">
          <stop offset="0" stop-color="#1f78c8" stop-opacity="0"/>
          <stop offset="0.5" stop-color="#1f78c8" stop-opacity="0.6"/>
          <stop offset="1" stop-color="#3fa4e0"/>
        </linearGradient>
      </defs>
      <path d="M0 40 C150 80 300 110 450 120 C600 125 760 110 876 80 V330 H0 Z" fill="url(#bottom-fade)"/>
      <path d="M60 330 C110 260 180 210 270 190 C330 230 360 290 370 330 Z" fill="#3fa4e0"/>
      <path d="M330 330 C380 270 460 250 540 250 C590 280 620 310 630 330 Z" fill="#eaf5fc"/>
      <path d="M0 190 C40 210 80 250 105 330 H0 Z" fill="#f2f8fc"/>
      <path d="M634 330 C660 260 720 215 800 205 C840 210 860 220 876 230 V330 Z" fill="#f2f8fc"/>
      <path d="M737 160 C760 130 800 120 840 130 C870 140 876 160 876 175 C850 195 800 205 760 195 C740 185 733 172 737 160 Z" fill="#fbed22"/>
    </svg>
  </main>
</body>
</html>
```